CRPG is needing business cards, and stationary created.

Pixel Forge created a logo for our business, and now we are wanting business cards, and stationary. I have included two designs of the same logo. Please feel free to use them as you want. The name of the company is Cedar Ridge Property Group LLC, the address is 812 NE Willow Ln., Suite 9, the city & state is Bend, Oregon, zip code is 97815, Telephone number is 541-327-4489, Fax number is 541-327-6051, the name on the business card is Carl Whitby CMCA

Industry/Entity Type

Property Management

Contact Information for Business Card

The card needs to look professional. Upscale.

Requirements
Must have
• The colors we are using are on the logo that has been uploaded.

```html
<!DOCTYPE html>
<html lang="en">
<head>
<meta charset="utf-8">
<title>Cedar Ridge Property Group — Stationery</title>
<link rel="stylesheet" href="https://fonts.googleapis.com/css2?family=Open+Sans:wght@400;600&family=Saira:wght@700&display=swap">
<style>
  :root {
    --ink: #000000;
    --teal: #1a8e7c;
    --teal-soft: #b9ddd6;
    --slate: #4b5563;
    --grey-soft: #c5c8ce;
    --paper: #ffffff;
    --text-muted: #4f5a63;
  }
  * { box-sizing: border-box; margin: 0; padding: 0; }
  html, body { width: 1200px; height: 902px; overflow: hidden; background: var(--paper); }
  body { position: relative; font-family: "Open Sans", Arial, sans-serif; }

  .brand { display: flex; align-items: center; gap: 8px; }
  .brand-mark { width: 14px; height: 14px; background: var(--teal); flex: none; }
  .brand-name { font-family: "Open Sans", Arial, sans-serif; font-weight: 600; color: var(--teal); letter-spacing: 1px; text-transform: uppercase; line-height: 1.1; }

  /* Letterhead strip */
  .letterhead {
    position: absolute; left: 60px; top: 80px; width: 560px; height: 150px;
    background: var(--ink); border-bottom: 14px solid var(--teal);
    display: flex; justify-content: space-between; align-items: center; padding: 0 28px;
  }
  .letterhead .brand-name { font-size: 24px; }
  .letterhead .brand-mark { width: 22px; height: 22px; }
  .letterhead .brand-sub { font-size: 9px; color: var(--text-muted); letter-spacing: 1.5px; margin-top: 4px; text-transform: uppercase; }
  .letterhead .brand-tag { font-size: 7px; color: var(--text-muted); letter-spacing: 4px; margin-top: 3px; text-transform: uppercase; }

  .contact { font-size: 10px; color: var(--text-muted); line-height: 1.45; }
  .contact li { list-style: none; display: flex; align-items: flex-start; gap: 6px; }
  .contact svg { width: 10px; height: 10px; flex: none; margin-top: 2px; fill: var(--teal); }
  .letterhead .contact { text-align: right; font-size: 11px; }
  .letterhead .contact li { justify-content: flex-end; }

  /* Business cards */
  .card {
    position: absolute; width: 210px; height: 330px; border-radius: 18px;
    background: var(--ink); border: 4px solid var(--teal);
    padding: 24px 18px; display: flex; flex-direction: column; align-items: center;
  }
  .card .brand-name { font-size: 17px; text-align: center; }
  .card .brand-sub { font-size: 7px; color: var(--text-muted); letter-spacing: 1px; text-transform: uppercase; margin-top: 4px; text-align: center; }
  .card .brand-tag { font-size: 6px; color: var(--text-muted); letter-spacing: 3px; text-transform: uppercase; margin-top: 2px; text-align: center; }
  .card .holder { margin-top: 64px; text-align: center; }
  .card .holder-name { font-size: 14px; color: var(--teal); }
  .card .holder-title { font-size: 10px; color: var(--text-muted); }
  .card .contact { margin-top: 14px; }
  .card-a { left: 680px; top: 80px; }
  .card-b { left: 940px; top: 300px; }
  .card-c { left: 120px; top: 520px; }

  /* Centre display name */
  .display-name {
    position: absolute; left: 380px; top: 400px; width: 420px; text-align: center;
    font-weight: 600; font-size: 46px; letter-spacing: 2px; color: var(--grey-soft); text-transform: uppercase;
  }

  /* Envelope flap edge */
  .envelope-edge {
    position: absolute; left: 480px; top: 700px; width: 520px; height: 22px;
    background: var(--ink); border-bottom: 10px solid var(--teal);
  }
</style>
</head>
<body>

<svg width="0" height="0" style="position:absolute">
  <symbol id="icon-phone" viewBox="0 0 24 24"><path d="M6.6 10.8a15.1 15.1 0 0 0 6.6 6.6l2.2-2.2a1 1 0 0 1 1-.25 11.4 11.4 0 0 0 3.6.57 1 1 0 0 1 1 1V20a1 1 0 0 1-1 1A17 17 0 0 1 3 4a1 1 0 0 1 1-1h3.5a1 1 0 0 1 1 1c0 1.25.2 2.45.57 3.57a1 1 0 0 1-.25 1z"/></symbol>
  <symbol id="icon-fax" viewBox="0 0 24 24"><path d="M6 2h10v6H6zM3 9h18v11H3zm3 3v2h2v-2zm4 0v2h2v-2zm4 0v2h4v-2z"/></symbol>
  <symbol id="icon-pin" viewBox="0 0 24 24"><path d="M12 2a7 7 0 0 0-7 7c0 5 7 13 7 13s7-8 7-13a7 7 0 0 0-7-7zm0 9.5A2.5 2.5 0 1 1 12 6.5a2.5 2.5 0 0 1 0 5z"/></symbol>
</svg>

<header class="letterhead">
  <div>
    <div class="brand"><span class="brand-mark"></span><span class="brand-name">Cedar Ridge</span></div>
    <p class="brand-sub">Property Group</p>
    <p class="brand-tag">Rooted in every detail</p>
  </div>
  <ul class="contact">
    <li>541-327-4489 <svg><use href="#icon-phone"/></svg></li>
    <li>541-327-6051 <svg><use href="#icon-fax"/></svg></li>
    <li>812 NE Willow Ln., Suite 9,<br>the city &amp; state is Bend,<br>Oregon, zip code is 97815 <svg><use href="#icon-pin"/></svg></li>
  </ul>
</header>

<article class="card card-a">
  <div class="brand"><span class="brand-mark"></span><span class="brand-name">Cedar Ridge</span></div>
  <p class="brand-sub">Property Group</p>
  <p class="brand-tag">Rooted in every detail</p>
  <div class="holder"><p class="holder-name">Carl Whitby</p><p class="holder-title">CMCA</p></div>
  <ul class="contact">
    <li><svg><use href="#icon-phone"/></svg>541-327-4489</li>
    <li><svg><use href="#icon-fax"/></svg>541-327-6051</li>
    <li>812 NE Willow Ln., Suite 9,<br>the city &amp; state is Bend,<br>Oregon, zip code is 97815</li>
  </ul>
</article>

<article class="card card-b">
  <div class="brand"><span class="brand-mark"></span><span class="brand-name">Cedar Ridge</span></div>
  <p class="brand-sub">Property Group</p>
  <p class="brand-tag">Rooted in every detail</p>
  <div class="holder"><p class="holder-name">Carl Whitby</p><p class="holder-title">CMCA</p></div>
  <ul class="contact">
    <li><svg><use href="#icon-phone"/></svg>541-327-4489</li>
    <li><svg><use href="#icon-fax"/></svg>541-327-6051</li>
    <li>812 NE Willow Ln., Suite 9,<br>the city &amp; state is Bend,<br>Oregon, zip code is 97815</li>
  </ul>
</article>

<article class="card card-c">
  <div class="brand"><span class="brand-mark"></span><span class="brand-name">Cedar Ridge</span></div>
  <p class="brand-sub">Property Group</p>
  <p class="brand-tag">Rooted in every detail</p>
  <div class="holder"><p class="holder-name">Carl Whitby</p><p class="holder-title">CMCA</p></div>
  <ul class="contact">
    <li><svg><use href="#icon-phone"/></svg>541-327-4489</li>
    <li><svg><use href="#icon-fax"/></svg>541-327-6051</li>
    <li>812 NE Willow Ln., Suite 9,<br>the city &amp; state is Bend,<br>Oregon, zip code is 97815</li>
  </ul>
</article>

<p class="display-name">Cedar Ridge</p>

<div class="envelope-edge"></div>

</body>
</html>
```